Thriving Through Slimming Book Cover

I need an eBook cover for my book
Title: Thriving Through Slimming - Steer Your Thoughts, Shape Your Frame
Subtitle: Bid Farewell to Seesaw Eating and Welcome Decades of Vigor and Joy
Author: Martin Kessler

This book is about learning the mechanisms behind weight loss and how to cultivate two qualities: discipline and consistency

Weight Loss, Mind Hack

• I would like to see 2 images of the same woman standing back to back. The one on the left is overweight and sad and the one on the right is not overweight and smiling.

```html
<!DOCTYPE html>
<html lang="en">
<head>
<meta charset="utf-8">
<title>Thriving Through Slimming – Book Cover</title>
<link rel="stylesheet" href="https://fonts.googleapis.com/css2?family=Bebas+Neue&family=Oswald:wght@400&family=Jost:wght@500&display=swap">
<style>
  :root {
    --page: #ffffff;
    --sky-top: #3d8fb0;
    --sky-mid: #8fd0d6;
    --sand: #f3dc8e;
    --amber: #e1a43c;
    --rust: #8c4a1c;
    --title-violet: #3b3496;
    --title-teal: #137a86;
    --tag-red: #d4482a;
    --ink: #111111;
    --author: #ffffff;
    --figure-blue: #2f45c9;
    --figure-light: #4a62e0;
  }
  * { margin: 0; padding: 0; box-sizing: border-box; }
  html, body { width: 1200px; height: 1200px; overflow: hidden; background: var(--page); }

  .canvas { position: relative; width: 1200px; height: 1200px; }

  .book-cover {
    position: absolute; left: 360px; top: 240px; width: 480px; height: 720px;
    background:
      radial-gradient(ellipse at 50% 110%, rgba(140,74,28,0.55), transparent 60%),
      linear-gradient(180deg, var(--sky-top) 0%, var(--sky-mid) 32%, var(--sand) 55%, var(--amber) 80%, var(--rust) 100%);
    text-align: center;
    overflow: hidden;
  }

  .cover-illustration {
    position: absolute; left: 112px; top: 54px; width: 262px; height: 236px;
  }

  .title-main {
    position: absolute; left: 0; right: 0;
    font-family: 'Bebas Neue', sans-serif;
    line-height: 1;
    background: linear-gradient(90deg, var(--title-violet), var(--title-teal) 60%, var(--title-violet));
    -webkit-background-clip: text; background-clip: text; color: transparent;
    filter: drop-shadow(2px 3px 2px rgba(0,0,0,0.35));
  }
  .title-top { top: 306px; font-size: 114px; letter-spacing: 2px; }
  .title-bottom { top: 440px; font-size: 104px; letter-spacing: 2px;
    background: linear-gradient(90deg, var(--title-teal), var(--title-violet) 55%, var(--title-violet));
    -webkit-background-clip: text; background-clip: text; }

  .title-joiner {
    position: absolute; left: 0; right: 0; top: 412px;
    display: flex; align-items: center; justify-content: center; gap: 12px;
    font-family: 'Bebas Neue', sans-serif; font-size: 30px; color: var(--ink); line-height: 1;
  }
  .title-joiner .rule { width: 96px; height: 2px; background: var(--ink); }

  .tagline {
    position: absolute; left: 0; right: 0; top: 545px;
    font-family: 'Oswald', sans-serif; font-size: 24px; line-height: 31px;
    letter-spacing: 7px; color: var(--tag-red); text-transform: uppercase;
  }

  .subtitle {
    position: absolute; left: 20px; right: 20px; top: 609px;
    font-family: 'Oswald', sans-serif; font-size: 19px; line-height: 30px;
    color: var(--ink); text-transform: uppercase;
  }

  .author {
    position: absolute; left: 0; right: 0; top: 678px;
    font-family: 'Jost', sans-serif; font-weight: 500; font-size: 17px;
    letter-spacing: 12px; color: var(--author); text-transform: uppercase;
  }
</style>
</head>
<body>
<div class="canvas">
  <div class="book-cover">
    <svg class="cover-illustration" viewBox="0 0 262 236" role="img"
         aria-label="Two blue dress forms back to back: a fuller figure on the left and a slimmer figure on the right">
      <defs>
        <linearGradient id="figure-shade" x1="0" y1="0" x2="1" y2="0">
          <stop offset="0" stop-color="var(--figure-blue)"/>
          <stop offset="0.5" stop-color="var(--figure-light)"/>
          <stop offset="1" stop-color="var(--figure-blue)"/>
        </linearGradient>
      </defs>
      <rect class="figure-before" x="0" y="0" width="134" height="236" rx="50" fill="url(#figure-shade)" opacity="0.8"/>
      <rect class="figure-after" x="156" y="0" width="106" height="236" rx="42" fill="url(#figure-shade)" opacity="0.8"/>
    </svg>

    <div class="title-main title-top">Thriving</div>
    <div class="title-joiner"><span class="rule"></span>Through<span class="rule"></span></div>
    <div class="title-main title-bottom">Slimming</div>

    <div class="tagline">Steer Your Thoughts<br>Shape Your Frame</div>
    <div class="subtitle">Bid Farewell to Seesaw Eating and Welcome Decades<br>of Vigor and Joy</div>
    <div class="author">Martin Kessler</div>
  </div>
</div>
</body>
</html>
```